VELORIND Multistep design - needs to match our existing design.

We have a multistep form(7 pages) we need the design for (rest of the website is done).
The multistep form is a vital part of the website, as it is the main service - so the form design should fit into the rest of the site.
Please take a look at the attached file - all about colors, fonts etc. is included in the file.

Target Market(s)

People looking for an interior architect in Denmark

Industry/Entity Type

Interior Design

Number of Pages Required

1 page

Requirements
Nice to have
• It's attached in the pdf file

```html
<!DOCTYPE html>
<html lang="da">
<head>
<meta charset="utf-8">
<title>VELORIND – Konceptet</title>
<link rel="stylesheet" href="https://fonts.googleapis.com/css2?family=PT+Sans:wght@400;700&family=Raleway:wght@300;400;700&family=Open+Sans:wght@600&display=swap">
<style>
  :root {
    --hero-dark: #1f2327;
    --hero-mid: #3a3836;
    --hero-warm: #5a4a3c;
    --slate: #33424f;
    --footer: #34434f;
    --white: #ffffff;
    --ink: #111111;
    --icon: #2f3a44;
    --btn-top: #ffffff;
    --btn-bottom: #d2d2d2;
    --badge: #e8213f;
    --chat-bubble: #2b3945;
  }
  * { box-sizing: border-box; margin: 0; padding: 0; }
  html, body { width: 1200px; height: 1019px; overflow: hidden; }
  body { position: relative; font-family: "PT Sans", sans-serif; background: var(--footer); }

  .hero { position: absolute; left: 0; top: 0; width: 1200px; height: 681px; }
  .hero-photo {
    position: absolute; inset: 0;
    background:
      radial-gradient(ellipse at 75% 35%, rgba(150,130,110,.45), transparent 55%),
      radial-gradient(ellipse at 30% 70%, rgba(110,90,70,.35), transparent 60%),
      linear-gradient(160deg, var(--hero-dark) 0%, var(--hero-mid) 45%, var(--hero-warm) 75%, var(--hero-dark) 100%);
  }
  .hero-photo::after { content: ""; position: absolute; inset: 0; background: rgba(20,24,28,.35); }

  .brand { position: absolute; left: 60px; top: 28px; font-size: 31px; color: var(--white); letter-spacing: .3px; }
  .nav { position: absolute; top: 33px; left: 490px; display: flex; list-style: none; }
  .nav li { font-size: 21px; color: var(--white); height: 41px; line-height: 41px; }
  .nav li + li { margin-left: 33px; }
  .nav .active { background: var(--white); color: var(--ink); padding: 0 15px; }
  .nav li:nth-child(2) { margin-left: 34px; }

  .rooms { position: absolute; left: 274px; top: 177px; width: 653px; height: 360px; }
  .room {
    position: absolute; width: 259px; height: 34px;
    background: linear-gradient(to bottom, var(--btn-top) 0%, #efefef 50%, var(--btn-bottom) 100%);
    color: var(--ink); font-size: 21px; line-height: 34px; padding-left: 26px;
  }
  .room svg { position: absolute; right: 17px; top: 6px; }
  .col-right { left: 395px; padding-left: 29px; }

  .continue {
    position: absolute; left: 411px; top: 570px; width: 350px; height: 49px;
    background: var(--slate); border-radius: 4px; color: var(--white);
    font-family: "Open Sans", sans-serif; font-weight: 600; font-size: 30px;
    text-align: center; line-height: 49px; letter-spacing: .5px;
  }

  .footer { position: absolute; left: 0; top: 681px; width: 1200px; height: 338px; background: var(--footer); color: var(--white); font-family: "Raleway", sans-serif; }
  .footer-brand { position: absolute; left: 0; width: 1200px; top: 92px; text-align: center; font-weight: 300; font-size: 37px; }
  .footer-col { position: absolute; text-align: center; font-size: 11px; line-height: 21.5px; font-weight: 300; }
  .footer-col b { font-weight: 700; }
  .about { left: 134px; width: 280px; top: 136px; }
  .contact { left: 500px; width: 200px; top: 156px; }
  .contact .gap { height: 22px; }
  .join { left: 770px; width: 312px; top: 136px; }

  .chat-prompt {
    position: absolute; left: 960px; top: 951px; width: 155px; height: 39px;
    background: var(--chat-bubble); border-radius: 20px; color: var(--white);
    font-family: "Open Sans", sans-serif; font-weight: 600; font-size: 12.5px; text-align: center; line-height: 39px;
  }
  .chat-button { position: absolute; left: 1124px; top: 943px; width: 53px; height: 53px; background: var(--chat-bubble); border-radius: 12px; }
  .chat-button svg { position: absolute; left: 14px; top: 15px; }
  .chat-badge {
    position: absolute; left: 1164px; top: 939px; width: 18px; height: 18px; border-radius: 50%;
    background: var(--badge); color: var(--white); font-size: 10px; font-family: "Open Sans", sans-serif; font-weight: 600;
    text-align: center; line-height: 18px;
  }
</style>
</head>
<body>
  <header class="hero">
    <div class="hero-photo" role="img" aria-label="Photo of an architect's hands drawing plans at a wooden desk with a ruler and rolled drawings"></div>
    <div class="brand">VELORIND</div>
    <ul class="nav">
      <li class="active">Konceptet</li>
      <li>Privat</li>
      <li>Erhverv</li>
      <li>Arkitekt</li>
      <li>Om VELORIND</li>
    </ul>

    <div class="rooms">
      <div class="room" style="top:0">Children’s room<svg width="23" height="23" viewBox="0 0 23 23"><circle cx="11.5" cy="11.5" r="10.3" fill="none" stroke="var(--icon)" stroke-width="1.8"/><path d="M11.5 6v11M6 11.5h11" stroke="var(--icon)" stroke-width="2.4"/></svg></div>
      <div class="room" style="top:57px">Office<svg width="23" height="23" viewBox="0 0 23 23"><circle cx="11.5" cy="11.5" r="10.3" fill="none" stroke="var(--icon)" stroke-width="1.8"/><path d="M11.5 6v11M6 11.5h11" stroke="var(--icon)" stroke-width="2.4"/></svg></div>
      <div class="room" style="top:113px">Kitchen<svg width="23" height="23" viewBox="0 0 23 23"><circle cx="11.5" cy="11.5" r="10.3" fill="none" stroke="var(--icon)" stroke-width="1.8"/><path d="M11.5 6v11M6 11.5h11" stroke="var(--icon)" stroke-width="2.4"/></svg></div>
      <div class="room" style="top:169px">Utility room<svg width="23" height="23" viewBox="0 0 23 23"><circle cx="11.5" cy="11.5" r="10.3" fill="none" stroke="var(--icon)" stroke-width="1.8"/><path d="M11.5 6v11M6 11.5h11" stroke="var(--icon)" stroke-width="2.4"/></svg></div>
      <div class="room" style="top:228px">Bathroom<svg width="23" height="23" viewBox="0 0 23 23"><circle cx="11.5" cy="11.5" r="10.3" fill="none" stroke="var(--icon)" stroke-width="1.8"/><path d="M11.5 6v11M6 11.5h11" stroke="var(--icon)" stroke-width="2.4"/></svg></div>
      <div class="room" style="top:285px">Patio<svg width="23" height="23" viewBox="0 0 23 23"><circle cx="11.5" cy="11.5" r="10.3" fill="none" stroke="var(--icon)" stroke-width="1.8"/><path d="M11.5 6v11M6 11.5h11" stroke="var(--icon)" stroke-width="2.4"/></svg></div>
      <div class="room" style="top:342px">Hobby room<svg width="23" height="23" viewBox="0 0 23 23"><circle cx="11.5" cy="11.5" r="10.3" fill="none" stroke="var(--icon)" stroke-width="1.8"/><path d="M11.5 6v11M6 11.5h11" stroke="var(--icon)" stroke-width="2.4"/></svg></div>

      <div class="room col-right" style="top:0">Bedroom<svg width="23" height="23" viewBox="0 0 23 23"><circle cx="11.5" cy="11.5" r="10.3" fill="none" stroke="var(--icon)" stroke-width="1.8"/><path d="M11.5 6v11M6 11.5h11" stroke="var(--icon)" stroke-width="2.4"/></svg></div>
      <div class="room col-right" style="top:57px">Living room<svg width="23" height="23" viewBox="0 0 23 23"><circle cx="11.5" cy="11.5" r="10.3" fill="none" stroke="var(--icon)" stroke-width="1.8"/><path d="M11.5 6v11M6 11.5h11" stroke="var(--icon)" stroke-width="2.4"/></svg></div>
      <div class="room col-right" style="top:113px">Kitchen-dining area<svg width="23" height="23" viewBox="0 0 23 23"><circle cx="11.5" cy="11.5" r="10.3" fill="none" stroke="var(--icon)" stroke-width="1.8"/><path d="M11.5 6v11M6 11.5h11" stroke="var(--icon)" stroke-width="2.4"/></svg></div>
      <div class="room col-right" style="top:169px">Entrance hall<svg width="23" height="23" viewBox="0 0 23 23"><circle cx="11.5" cy="11.5" r="10.3" fill="none" stroke="var(--icon)" stroke-width="1.8"/><path d="M11.5 6v11M6 11.5h11" stroke="var(--icon)" stroke-width="2.4"/></svg></div>
      <div class="room col-right" style="top:228px">Basement<svg width="23" height="23" viewBox="0 0 23 23"><circle cx="11.5" cy="11.5" r="10.3" fill="none" stroke="var(--icon)" stroke-width="1.8"/><path d="M11.5 6v11M6 11.5h11" stroke="var(--icon)" stroke-width="2.4"/></svg></div>
      <div class="room col-right" style="top:285px">Outdoor area<svg width="23" height="23" viewBox="0 0 23 23"><circle cx="11.5" cy="11.5" r="10.3" fill="none" stroke="var(--icon)" stroke-width="1.8"/><path d="M11.5 6v11M6 11.5h11" stroke="var(--icon)" stroke-width="2.4"/></svg></div>
      <div class="room col-right" style="top:342px">The whole house<svg width="23" height="23" viewBox="0 0 23 23"><circle cx="11.5" cy="11.5" r="10.3" fill="none" stroke="var(--icon)" stroke-width="1.8"/><path d="M11.5 6v11M6 11.5h11" stroke="var(--icon)" stroke-width="2.4"/></svg></div>
    </div>

    <div class="continue">CONTINUE</div>
  </header>

  <footer class="footer">
    <div class="footer-brand">VELORIND</div>
    <p class="footer-col about">VELORIND er din portal, hvor du kan indhente to gratis matches på arkitekter til din indretningsopgave. Du udfylder alle oplysninger om din opgave, og vores database udregner det bedste match til dig – helt uforpligtende og gratis.<br>Kom igang lige <b>her</b></p>
    <p class="footer-col contact">Kildebakken 14<br>8600, Silkeborg<span class="gap" style="display:block"></span>+45 00 00 00 00<br>info@velorind.dk</p>
    <p class="footer-col join"><b>Er du arkitekt?</b><br>Ønsker du at blive en del af VELORIND, så klik <b>her</b> og bliv nemt en del af vores arkitektdatabase.</p>
  </footer>

  <div class="chat-prompt">What's your question?</div>
  <div class="chat-button">
    <svg width="26" height="24" viewBox="0 0 26 24"><path d="M3 2h20a2 2 0 0 1 2 2v11a2 2 0 0 1-2 2H12l-5 5v-5H3a2 2 0 0 1-2-2V4a2 2 0 0 1 2-2z" fill="var(--white)"/><rect x="6" y="6.5" width="14" height="6" rx="1" fill="var(--chat-bubble)"/></svg>
  </div>
  <div class="chat-badge">1</div>
</body>
</html>
```